KMB and Employer Sleep Apnea Screening - BROCHURE

Brochure for marketing to KMB Clinics and directly to Employers of commercial drivers for screening of Sleep Apnea. We are a diagnostic sleep facility that offers In-Lab sleep testing and Home sleep testing. Our website: bluperinhealth.com

I put together an idea but i’m Not a designer and welcome your ideas for a brochure.

Two Sided Brochure
TRIM: 99 mm Wide x 210 mm High
with Bleed 105 mm Wide x 216 mm High
allow a 4 mm around card for critical elements

The idea is to print 3 handouts to a 8.5" x 11" card sheet with printing on front and back.
Updates

We are looking for a brochure not a flyer. First time using site and did not see option for brochure. We are looking for a brochure. Thank you for your designs and input.

Target Market(s)

Commercial Truck Drivers

Colors

Designer to choose colors to be used in the design.

Requirements
Must have
• Website: bluperinhealth.com
• Low Out-of-Pocket Cost and Most Insurances Accepted
• Quick Turn Around Time for Sleep Results
• PWRE Accredited
Nice to have
• Images of Commercial Truck or Truck Drivers

```html
<!DOCTYPE html>
<html lang="en">
<head>
<meta charset="utf-8">
<title>Bluperin Health – KMB Sleep Apnea Screening Brochure</title>
<link rel="stylesheet" href="https://fonts.googleapis.com/css2?family=Montserrat:wght@500;700;800;900&family=Open+Sans:wght@400;600;700&display=swap">
<style>
  :root{
    --blue:#1e88d2;
    --blue-dark:#135f9c;
    --navy:#1d2a38;
    --yellow:#f5c518;
    --white:#ffffff;
    --ink:#2b2f36;
    --grey-photo-a:#9a9fa6;
    --grey-photo-b:#4b5058;
    --stage:#dfe2e6;
  }
  *{box-sizing:border-box;margin:0;padding:0}
  html,body{width:835px;height:1200px;overflow:hidden;background:var(--stage)}
  body{font-family:"Open Sans",Arial,sans-serif;color:var(--ink);position:relative}

  .spread{position:absolute;left:153px;width:528px;height:560px;display:flex;box-shadow:0 2px 8px rgba(0,0,0,.18)}
  .spread--outside{top:25px}
  .spread--inside{top:615px}
  .panel{position:relative;width:264px;height:560px;overflow:hidden;background:var(--white)}
  .panel + .panel{border-left:1px solid rgba(0,0,0,.08)}

  .photo{position:absolute;display:block}
  .heading{font-family:"Montserrat",Arial,sans-serif;font-weight:900;text-transform:uppercase;line-height:1.05}
  .brand-line{font-family:"Montserrat",Arial,sans-serif;font-weight:700;font-size:9px;letter-spacing:.12em;text-transform:uppercase}
  .phone{font-family:"Montserrat",Arial,sans-serif;font-weight:800;letter-spacing:.01em}

  /* Back cover */
  .back-photo{left:0;top:0;width:100%;height:330px;background:linear-gradient(150deg,var(--grey-photo-a),var(--grey-photo-b))}
  .back-band{position:absolute;inset:0;background:var(--blue);clip-path:polygon(0 60%,100% 47%,100% 100%,0 100%)}
  .back-deco{position:absolute;right:0;top:0}
  .back-contact{position:absolute;left:22px;bottom:40px;color:var(--white)}
  .back-contact .phone{font-size:25px;margin-top:6px}
  .back-contact .call{font-family:"Montserrat",Arial,sans-serif;font-weight:800;font-size:18px;margin-top:4px}

  /* Front cover */
  .front-top-deco{position:absolute;left:0;top:0}
  .front-head{position:absolute;right:16px;top:48px;text-align:right;color:var(--white);width:190px}
  .front-head .brand-line{color:var(--white)}
  .front-head .phone{font-size:18px;margin:4px 0 10px}
  .front-head .heading{font-size:17px}
  .front-photo{left:0;top:250px;width:100%;height:230px;background:linear-gradient(170deg,#c9d3dc 0%,#8c959e 55%,#d49a2a 100%)}
  .front-foot{position:absolute;left:0;bottom:0;width:100%;height:80px;background:var(--blue);clip-path:polygon(0 30%,100% 0,100% 100%,0 100%)}
  .cta{position:absolute;left:22px;bottom:22px;background:var(--yellow);color:var(--navy);font-family:"Montserrat",Arial,sans-serif;font-weight:800;font-size:13px;padding:7px 16px;letter-spacing:.04em}

  /* Inside left */
  .stress{position:absolute;left:0;top:0;width:100%;height:300px}
  .stress-copy{position:absolute;left:16px;top:18px;width:140px}
  .stress-copy .heading{color:var(--blue);font-size:18px}
  .stress-copy p{font-size:7.5px;line-height:1.45;margin:5px 0 12px;color:var(--ink)}
  .checklist{list-style:none;background:var(--blue);color:var(--white);padding:9px 8px;font-size:7.5px;font-weight:600}
  .checklist li{display:flex;align-items:center;gap:5px;margin:4px 0}
  .stress-photo{right:0;top:0;width:100px;height:300px;background:linear-gradient(180deg,#e9eef3,#c7cfd8)}
  .sleep-photo{left:0;top:300px;width:100%;height:160px;background:linear-gradient(120deg,#f1e4d6,#d9c3ae 60%,#eef1f4)}
  .inside-foot{position:absolute;left:0;bottom:0;width:100%;height:100px;background:var(--blue);color:var(--white);padding:24px 18px 0;clip-path:polygon(0 18%,100% 0,100% 100%,0 100%)}
  .inside-foot .phone{font-size:22px;margin-top:5px}

  /* Inside right */
  .logo{position:absolute;left:16px;top:20px;display:flex;align-items:center;gap:7px;font-family:"Open Sans",Arial,sans-serif;font-weight:700;font-size:13px;color:var(--blue)}
  .logo-dot{width:16px;height:16px;border-radius:50%;background:var(--blue)}
  .badge{position:absolute;right:16px;top:12px;width:38px;height:38px;border-radius:50%;background:var(--blue-dark)}
  .right-photo{left:0;top:62px;width:100%;height:150px;background:linear-gradient(100deg,#eef2f5,#d7c2ad 55%,#f3f5f7)}
  .insurances{position:absolute;left:0;top:212px;width:100%;height:270px;background:var(--blue);color:var(--white);padding:16px 18px}
  .insurances .heading{font-size:17px;text-align:center}
  .insurances .sub{font-size:7.5px;text-align:center;margin:4px 0 10px}
  .plan-list{list-style:none;columns:2;column-gap:14px;font-size:8px;line-height:1.9}
  .plan-list li::before{content:"•";margin-right:4px}
  .contact-bar{position:absolute;left:0;bottom:0;width:100%;height:78px;background:var(--navy);color:var(--white);padding:12px 18px;font-size:7.5px;line-height:1.6}
  .contact-bar .web{font-family:"Montserrat",Arial,sans-serif;font-weight:700;font-size:10px;color:var(--yellow)}
  .contact-row{display:flex;align-items:center;gap:6px}
</style>
</head>
<body>

<section class="spread spread--outside">
  <article class="panel panel--back">
    <div class="photo back-photo" role="img" aria-label="Black and white photo of a driver's hands on a truck steering wheel"></div>
    <svg class="back-deco" width="120" height="150" viewBox="0 0 120 150" aria-hidden="true">
      <polygon points="40,0 120,0 120,110" fill="var(--blue)" opacity=".85"/>
      <polygon points="78,0 120,0 120,60" fill="var(--blue-dark)"/>
    </svg>
    <div class="back-band"></div>
    <div class="back-contact">
      <div class="brand-line">Bluperin Health</div>
      <div class="phone">702-555-0148</div>
      <div class="call">CALL TODAY</div>
    </div>
  </article>

  <article class="panel panel--front">
    <svg class="front-top-deco" width="264" height="250" viewBox="0 0 264 250" aria-hidden="true">
      <polygon points="0,0 264,0 264,240 0,170" fill="var(--blue)"/>
      <polygon points="0,0 90,0 0,80" fill="var(--blue-dark)"/>
    </svg>
    <div class="front-head">
      <div class="brand-line">Bluperin Health</div>
      <div class="phone">702-555-0148</div>
      <h1 class="heading">KMB Physical requires testing for sleep apnea</h1>
    </div>
    <div class="photo front-photo" role="img" aria-label="Photo of two workers in hard hats beside an orange dump truck"></div>
    <div class="front-foot"></div>
    <div class="cta">CALL TODAY</div>
  </article>
</section>

<section class="spread spread--inside">
  <article class="panel panel--inside-left">
    <div class="stress">
      <div class="photo stress-photo" role="img" aria-label="Illustration of a tired driver yawning at the wheel"></div>
      <div class="stress-copy">
        <h2 class="heading">Don't stress</h2>
        <p>Keep your medical card and stay on the road.</p>
        <ul class="checklist">
          <li><svg width="8" height="8" viewBox="0 0 8 8"><path d="M1 4l2 2 4-5" stroke="#fff" stroke-width="1.4" fill="none"/></svg>Low out-of-pocket cost</li>
          <li><svg width="8" height="8" viewBox="0 0 8 8"><path d="M1 4l2 2 4-5" stroke="#fff" stroke-width="1.4" fill="none"/></svg>Most insurances accepted</li>
          <li><svg width="8" height="8" viewBox="0 0 8 8"><path d="M1 4l2 2 4-5" stroke="#fff" stroke-width="1.4" fill="none"/></svg>Quick turnaround for results</li>
          <li><svg width="8" height="8" viewBox="0 0 8 8"><path d="M1 4l2 2 4-5" stroke="#fff" stroke-width="1.4" fill="none"/></svg>PWRE accredited facility</li>
          <li><svg width="8" height="8" viewBox="0 0 8 8"><path d="M1 4l2 2 4-5" stroke="#fff" stroke-width="1.4" fill="none"/></svg>Test in your own bed</li>
        </ul>
        <h2 class="heading" style="font-size:15px;margin-top:12px">Don't wait</h2>
        <p>Book your home sleep test today.</p>
      </div>
    </div>
    <div class="photo sleep-photo" role="img" aria-label="Photo of a woman sleeping peacefully on a white pillow"></div>
    <div class="inside-foot">
      <div class="brand-line">Bluperin Health</div>
      <div class="phone">702-555-0148</div>
    </div>
  </article>

  <article class="panel panel--inside-right">
    <div class="logo"><span class="logo-dot"></span>Bluperin Health</div>
    <div class="badge" role="img" aria-label="PWRE accreditation badge"></div>
    <div class="photo right-photo" role="img" aria-label="Photo of a woman asleep in bed wearing a home sleep test sensor"></div>
    <div class="insurances">
      <h2 class="heading">Insurances</h2>
      <p class="sub">Low out-of-pocket cost, most plans accepted</p>
      <ul class="plan-list">
        <li>Northway Health</li><li>Crestline Care</li><li>Harbor Mutual</li><li>Summit Plan</li>
        <li>Bayfield Health</li><li>Pinecrest Care</li><li>Lakeview Plan</li><li>Redstone Mutual</li>
        <li>Fairhaven Health</li><li>Oakridge Care</li><li>Silverline Plan</li><li>Westbrook Mutual</li>
        <li>Meadow Health</li><li>Granite Care</li><li>Clearwater Plan</li><li>Ironwood Mutual</li>
      </ul>
    </div>
    <div class="contact-bar">
      <div class="contact-row"><svg width="8" height="10" viewBox="0 0 8 10"><path d="M4 0a3.5 3.5 0 0 0-3.5 3.5C.5 6 4 10 4 10s3.5-4 3.5-6.5A3.5 3.5 0 0 0 4 0z" fill="#fff"/></svg>4415 Desert Ridge Blvd, Suite 120, Las Vegas NV</div>
      <div class="contact-row"><svg width="9" height="9" viewBox="0 0 24 24"><path d="M6.6 10.8a15 15 0 0 0 6.6 6.6l2.2-2.2c.3-.3.7-.4 1-.2 1.1.4 2.3.6 3.6.6.6 0 1 .4 1 1V20c0 .6-.4 1-1 1A17 17 0 0 1 3 4c0-.6.4-1 1-1h3.5c.6 0 1 .4 1 1 0 1.3.2 2.5.6 3.6.1.3 0 .7-.2 1z" fill="#fff"/></svg>702-555-0148</div>
      <div class="web">bluperinhealth.com</div>
    </div>
  </article>
</section>

</body>
</html>
```